Private Investment Partnership needs Business Card Design

We are a brand-new private investment partnership looking for business card design help. It will be called The Corvale + Vantry Partnership. We are based in NYC (hence Corvale) and our other partner is a firm called Vantry Resources which has roots in Pittsburgh, PA. We are looking for something a bit more formal and professional- probably typographic oriented in a font like Adobe Garamond. We might want to incorporate the colors PMS Yellow 1235 and PMS Blue 282. Attached is a pretty plain, old example of something.

```html
<!DOCTYPE html>
<html lang="en">
<head>
<meta charset="utf-8">
<title>Corvale Vantry Partnership – Business Card</title>
<link rel="stylesheet" href="https://fonts.googleapis.com/css2?family=Arimo:wght@400;700&family=EB+Garamond:wght@400;500&display=swap">
<style>
  :root {
    --pms-yellow: #f9b526;
    --pms-blue: #03264a;
    --ink-blue: #0d2b52;
    --paper: #ffffff;
  }
  html, body {
    margin: 0;
    padding: 0;
    width: 1200px;
    height: 1200px;
    overflow: hidden;
    background: var(--paper);
  }
  .canvas {
    position: relative;
    width: 1200px;
    height: 1200px;
  }
  .card {
    position: absolute;
    left: 350px;
    width: 462px;
    height: 283px;
  }
  .card--front { top: 209px; background: var(--pms-yellow); }
  .card--back  { top: 603px; background: var(--pms-blue); }

  .brand {
    position: absolute;
    left: 22px;
    top: 30px;
    display: flex;
    align-items: center;
    gap: 14px;
    color: var(--ink-blue);
    font-family: "Arimo", sans-serif;
    font-weight: 700;
  }
  .brand__mark {
    width: 46px;
    height: 46px;
    border: 4px solid var(--ink-blue);
    border-radius: 50%;
    box-sizing: border-box;
  }
  .brand__name { line-height: 1; }
  .brand__primary { display: block; font-size: 31px; }
  .brand__secondary { display: block; font-size: 15px; margin-top: 3px; }

  .contact-block {
    position: absolute;
    left: 220px;
    top: 188px;
    padding-left: 22px;
    border-left: 4px solid var(--ink-blue);
    color: var(--ink-blue);
  }
  .contact-block__name {
    font-family: "EB Garamond", serif;
    font-weight: 500;
    font-size: 20px;
    letter-spacing: 0.04em;
    line-height: 1;
    margin: 0 0 2px;
  }
  .contact-block__title {
    font-family: "EB Garamond", serif;
    font-size: 11px;
    letter-spacing: 0.16em;
    margin: 0 0 6px;
  }
  .contact-block__address {
    font-family: "Arimo", sans-serif;
    font-size: 11px;
    letter-spacing: 0.05em;
    line-height: 15px;
    margin: 0;
    font-style: normal;
  }

  .back-brand {
    position: absolute;
    left: 0;
    right: 0;
    top: 62px;
    display: flex;
    justify-content: center;
    align-items: center;
    gap: 12px;
    color: var(--pms-yellow);
    font-family: "Arimo", sans-serif;
    font-weight: 700;
    font-size: 28px;
  }
  .back-brand__mark {
    width: 56px;
    height: 56px;
    border: 4px solid var(--pms-yellow);
    border-radius: 50%;
    box-sizing: border-box;
  }
  .back-contact {
    position: absolute;
    left: 0;
    right: 0;
    top: 228px;
    text-align: center;
    color: var(--pms-yellow);
    font-family: "Arimo", sans-serif;
    font-size: 11px;
    letter-spacing: 0.08em;
    line-height: 15px;
  }
  .back-contact p { margin: 0; }
</style>
</head>
<body>
<main class="canvas">
  <section class="card card--front" aria-label="Card front">
    <div class="brand">
      <span class="brand__mark" aria-hidden="true"></span>
      <span class="brand__name">
        <span class="brand__primary">Corvale</span>
        <span class="brand__secondary">Vantry Partnership</span>
      </span>
    </div>
    <div class="contact-block">
      <h1 class="contact-block__name">DANIEL R. MORROW</h1>
      <p class="contact-block__title">CHIEF INVESTMENT OFFICER</p>
      <address class="contact-block__address">
        ARDENT FIELD CAPITAL, LLC<br>
        418 HARBOR VIEW AVENUE<br>
        STAMFORD, CT 06901
      </address>
    </div>
  </section>

  <section class="card card--back" aria-label="Card back">
    <div class="back-brand">
      <span class="back-brand__mark" aria-hidden="true"></span>
      <span>Corvale</span>
    </div>
    <div class="back-contact">
      <p>T: (203) 555-0148&nbsp;&nbsp;M: (646) 555-0192</p>
      <p>E: dmorrow@ardentfield.com</p>
    </div>
  </section>
</main>
</body>
</html>
```